General Contractors need a new Crisp updated Card Design

We need a new business card design for our company of 25 years based in Toronto call Holvaster Building Inc. : Our goal is to be the leading commercial contractors in Toronto by providing exceptional value to our clients. We work very hard to deliver professional, quality, service in conjunction with consistent price competitiveness to all of our clients on every single project.

Target Market(s)

Design & Build Clients

Industry/Entity Type

Construction Company

Contact Information for Business Card

Address:
18 North Tamlin Glen Road, Unit 57, Marbrook Vale, ON, K7T 2R9
Office: 905-218-5937

Holvasters Logo
Employee Job Description
Employee Cell Phone #
Employee Email
www.holvaster-example.com

Colors

Designer to choose colors to be used in the design.

Requirements
Must have
• Quote Company Saying:
• "Professional. Quality. Service."
Nice to have
• New Crisp up to date look. simple & fresh ( Not to Busy)
Should not have
• NO BLUE PRINTS ON THE BUSINESS CARDS

```html
<!DOCTYPE html>
<html lang="en">
<head>
<meta charset="utf-8">
<title>Holvaster Building Inc. — Business Card Back</title>
<link rel="stylesheet" href="https://fonts.googleapis.com/css2?family=Tinos&display=swap">
<style>
  :root {
    --ink-teal: #1a7565;
    --paper: #ffffff;
  }
  html, body {
    margin: 0;
    padding: 0;
    width: 1200px;
    height: 668px;
    overflow: hidden;
    background: var(--paper);
  }
  .card {
    position: relative;
    width: 1200px;
    height: 668px;
    background: var(--paper);
    color: var(--ink-teal);
    font-family: "Tinos", "Times New Roman", serif;
  }
  .card__slogan {
    position: absolute;
    top: 52px;
    left: 0;
    width: 1200px;
    margin: 0;
    text-align: center;
    font-size: 62px;
    font-weight: 400;
    line-height: 1.2;
  }
  .card__contact {
    position: absolute;
    top: 178px;
    left: 86px;
    width: 940px;
    margin: 0;
    padding: 0;
    list-style: none;
    font-size: 44px;
    line-height: 56.5px;
  }
  .card__rule {
    position: absolute;
    left: 70px;
    top: 577px;
  }
</style>
</head>
<body>
  <main class="card">
    <h1 class="card__slogan">Professional. Quality. Service.</h1>
    <ul class="card__contact">
      <li>Employee Job Description</li>
      <li>Employee Cell Phone</li>
      <li>Employee Email</li>
      <li>www.holvaster-example.com</li>
      <li>18 North Tamlin Glen Road, Unit 57, Marbrook Vale, ON, K7T 2R9 Office: 905-218-5937</li>
    </ul>
    <svg class="card__rule" width="1014" height="8" viewBox="0 0 1014 8" aria-hidden="true">
      <rect x="0" y="0" width="1014" height="8" fill="var(--ink-teal)"/>
    </svg>
  </main>
</body>
</html>
```